Elegant Business Card for Technology Company

Client is a supplier of innovative industrial communications and automation equipment since 2002. This contest is to gather fresh ideas for a redesign of the existing business card. Client is looking for design that best communicates tagline "Industrial Networking and Computing Specialist".

Design submissions should look modern, clean, elegant and professional. It should not be cluttered. Use white as the primary colour. Orange and black as secondary colour. Refer to jpeg File 1 on the current design.

Fonts used by Client used include Arial Regular, Arial Black, Roboto Regular, Roboto Black and Lato.

The winning design will be sent for offset printing using super white 250gsm artcard paper (open for suggestions).

Target Market(s)

System Engineers, Project Managers, Purchasing Managers from companies providing engineering services for Smart Cities.

Industry/Entity Type

Information Technology

Contact Information for Business Card

Refer to PDF File 3 for Business Card Details. Priority of short contact information would be as follows Name > Job Title > Email > Mobile > Web > Tel > Fax > Business Address >UEN (UEN represents company registration number)

Font styles to use
Sans Serif

Colors
ffffff
f37122
000000
5c5c5c

Requirements
Must have
• Refer to AI File 2 (Company Logo) & PDF File 3 (Information on Namecard)
Should not have
• No QR codes
• No Social Media Icons
• Do not create full Black or Orange colour background

```html
<!DOCTYPE html>
<html lang="en">
<head>
<meta charset="utf-8">
<title>KVS Business Card</title>
<link rel="stylesheet" href="https://fonts.googleapis.com/css2?family=Lato:wght@400;700;900&display=swap">
<style>
  :root {
    --white: #ffffff;
    --orange: #f37122;
    --black: #000000;
    --ink: #111111;
    --grey: #5c5c5c;
    --stage: #e9e9e7;
  }
  * { margin: 0; padding: 0; box-sizing: border-box; }
  html, body { width: 1200px; height: 1023px; overflow: hidden; }
  body {
    background: var(--stage);
    font-family: "Lato", sans-serif;
    position: relative;
  }
  .card {
    position: absolute;
    left: 300px;
    width: 600px;
    height: 340px;
    border-radius: 22px;
    overflow: hidden;
    background: var(--white);
    box-shadow: 0 10px 30px rgba(0,0,0,0.18);
  }
  .card-front { top: 110px; }
  .card-back  { top: 570px; background: linear-gradient(135deg, #ffffff 0%, #f2f2f2 100%); }

  /* Front */
  .front-panel { position: absolute; inset: 0; }
  .front-brand {
    position: absolute;
    left: 455px; top: 190px;
    display: flex; align-items: center; gap: 12px;
  }
  .brand-dot { width: 34px; height: 34px; border-radius: 50%; background: var(--orange); }
  .brand-name { font-weight: 900; font-size: 46px; letter-spacing: 1px; line-height: 1; }
  .front-brand .brand-name { color: var(--white); }
  .person { position: absolute; left: 38px; top: 34px; }
  .person-name { color: var(--orange); font-size: 28px; font-weight: 400; }
  .person-title { color: var(--grey); font-size: 15px; margin-top: 2px; }
  .contact-list { list-style: none; position: absolute; font-size: 15px; color: var(--ink); }
  .contact-list li { display: flex; align-items: center; gap: 10px; height: 22px; }
  .contact-list svg { width: 13px; height: 13px; flex: none; }
  .phones { left: 38px; top: 118px; }
  .online { left: 38px; top: 208px; }
  .address { position: absolute; left: 38px; top: 264px; display: flex; gap: 10px; font-size: 14px; line-height: 1.35; color: var(--ink); }
  .address svg { width: 14px; height: 14px; margin-top: 2px; flex: none; }
  .divider { position: absolute; left: 38px; top: 192px; width: 250px; height: 5px; background: var(--orange); }

  /* Back */
  .back-brand {
    position: absolute;
    left: 230px; top: 120px;
    display: flex; align-items: center; gap: 16px;
  }
  .back-brand .brand-dot { width: 54px; height: 54px; }
  .back-brand .brand-name { color: var(--black); font-size: 84px; }
  .tag-block { position: absolute; left: 0; bottom: 0; width: 600px; height: 80px; }
  .tagline {
    position: absolute; left: 100px; bottom: 44px;
    font-size: 15px; color: var(--ink);
  }
  .uen {
    position: absolute; left: 100px; bottom: 20px;
    font-size: 15px; color: var(--orange); letter-spacing: 4px;
  }
</style>
</head>
<body>

<section class="card card-front">
  <svg class="front-panel" width="600" height="340" viewBox="0 0 600 340" aria-hidden="true">
    <path d="M400 0 H600 V340 H400 V180 H370 L385 160 V0 Z" fill="var(--black)"/>
    <rect x="320" y="0" width="80" height="34" fill="var(--orange)"/>
    <rect x="320" y="34" width="14" height="306" fill="var(--orange)"/>
  </svg>

  <div class="person">
    <div class="person-name">Daniel Koh</div>
    <div class="person-title">Sales Manager</div>
  </div>

  <ul class="contact-list phones">
    <li><svg viewBox="0 0 14 14"><rect x="3" y="0.5" width="8" height="13" rx="1.5" fill="var(--orange)"/><rect x="4.5" y="2" width="5" height="8" fill="var(--white)"/></svg>+65 9123 4567</li>
    <li><svg viewBox="0 0 14 14"><path d="M3 1 L5.5 1 L6.5 4 L5 5.5 Q6.5 8.5 8.5 9 L10 7.5 L13 8.5 L13 11 Q12 13 9.5 13 Q2 11 1 3.5 Q1 1 3 1 Z" fill="var(--orange)"/></svg>+65 6123 4500</li>
    <li><svg viewBox="0 0 14 14"><rect x="1" y="5" width="12" height="8" rx="1" fill="var(--orange)"/><rect x="3.5" y="1" width="7" height="5" fill="var(--orange)"/><rect x="4" y="8" width="6" height="1.5" fill="var(--white)"/></svg>+65 6123 4501</li>
  </ul>

  <div class="divider"></div>

  <ul class="contact-list online">
    <li><svg viewBox="0 0 14 14"><rect x="0.5" y="2.5" width="13" height="9" fill="var(--orange)"/><path d="M0.5 2.5 L7 8 L13.5 2.5" stroke="var(--white)" stroke-width="1.2" fill="none"/></svg>sales@kvs-tech.sg</li>
    <li><svg viewBox="0 0 14 14"><circle cx="7" cy="7" r="6" fill="none" stroke="var(--orange)" stroke-width="1.4"/><ellipse cx="7" cy="7" rx="2.6" ry="6" fill="none" stroke="var(--orange)" stroke-width="1.2"/><line x1="1" y1="7" x2="13" y2="7" stroke="var(--orange)" stroke-width="1.2"/></svg>www.kvs-tech.sg</li>
  </ul>

  <div class="address">
    <svg viewBox="0 0 14 14"><path d="M7 1 L13 7 H11 V13 H3 V7 H1 Z" fill="var(--orange)"/><rect x="6" y="9" width="2" height="4" fill="var(--white)"/></svg>
    <span>25 Harbour Link, Lumen Techpark #04-12<br>(Block B), Singapore 419870</span>
  </div>

  <div class="front-brand">
    <span class="brand-dot"></span>
    <span class="brand-name">KVS</span>
  </div>
</section>

<section class="card card-back">
  <div class="back-brand">
    <span class="brand-dot"></span>
    <span class="brand-name">KVS</span>
  </div>

  <svg class="tag-block" width="600" height="80" viewBox="0 0 600 80" aria-hidden="true">
    <path d="M0 34 H70 V80 H0 Z" fill="var(--black)"/>
    <path d="M70 72 H420 V80 H70 Z" fill="var(--black)"/>
    <path d="M420 50 H600 V80 H420 Z" fill="var(--black)"/>
  </svg>
  <div class="tagline">Industrial Networking and Computing Specialist</div>
  <div class="uen">UEN NO: 200207315K</div>
</section>

</body>
</html>
```